Original business card of a small accounting firm

My firm specializes in accounting and taxes for small businesses. I'm looking for an original and creative business card as a marketing tool to give to prospective clients; however since we are a professional firm the card must also appear professional. I'm uploading a few examples of what I believe may fit my needs. Please feel free to use them as a jumping off point. Lastly, I'm uploading the company logo which I'd like to be the focal point on the back of the card and somewhat incorporated on the front on a smaller scale. I hope my description was helpful.
Target Market(s)
Tax clients and small businesses
Industry/Entity Type
Accounting
Contact Information for Business Card
Gerald Whitcombe
Certified Public Accountant │President
Whitcombe Advisors
T│ (555) 417-2863
Email│GWhitcombe@WhitcombeAdvisors.example
Look and feel
Each slider illustrates characteristics of the customer's brand and the style your logo design should communicate.

```html
<!DOCTYPE html>
<html lang="en">
<head>
<meta charset="utf-8">
<title>Whitcombe Advisors – Business Card</title>
<link rel="stylesheet" href="https://fonts.googleapis.com/css2?family=Arimo:wght@400;700&family=Michroma&family=Didact+Gothic&family=Cinzel:wght@400&display=swap">
<style>
  :root {
    --stage: #141518;
    --card-white: #ffffff;
    --card-navy: #070b22;
    --ink-gray: #4a4c50;
    --ink-dark: #2e3034;
    --brand-blue: #3f7fc4;
    --band-blue: #5b8fca;
    --band-gray: #555759;
    --silver: #a9adb3;
  }
  * { box-sizing: border-box; margin: 0; padding: 0; }
  html, body { width: 1200px; height: 871px; overflow: hidden; }
  body {
    background: var(--stage);
    display: flex;
    flex-direction: column;
    align-items: center;
    justify-content: center;
    gap: 36px;
  }
  .card {
    width: 680px;
    height: 388px;
    border-radius: 18px;
    position: relative;
    overflow: hidden;
  }

  /* Back */
  .card-back {
    background: var(--card-navy);
    display: flex;
    flex-direction: column;
    align-items: center;
    justify-content: center;
    gap: 10px;
  }
  .card-back .brand-row { display: flex; align-items: center; gap: 16px; }
  .card-back .brand-mark { width: 34px; height: 34px; background: var(--brand-blue); }
  .card-back .brand-name {
    font-family: "Arimo", sans-serif; font-weight: 700;
    font-size: 44px; color: var(--silver); letter-spacing: -0.5px;
  }
  .card-back .tagline {
    font-family: "Cinzel", serif; font-size: 15px;
    color: var(--silver); letter-spacing: 2.5px;
  }

  /* Front */
  .card-front { background: var(--card-white); }
  .front-body {
    position: absolute; left: 0; top: 0; right: 0; bottom: 30px;
    display: flex; align-items: center;
    padding: 0 26px 0 14px;
  }
  .brand-block {
    flex: 0 0 258px;
    display: flex; flex-direction: column; align-items: center; gap: 6px;
  }
  .brand-block .brand-row { display: flex; align-items: center; gap: 8px; }
  .brand-block .brand-mark { width: 18px; height: 18px; background: var(--brand-blue); }
  .brand-block .brand-name {
    font-family: "Arimo", sans-serif; font-weight: 700;
    font-size: 22px; color: var(--ink-gray); letter-spacing: -0.3px;
    white-space: nowrap;
  }
  .brand-block .tagline {
    font-family: "Cinzel", serif; font-size: 8.5px;
    color: var(--ink-gray); letter-spacing: 1.2px; white-space: nowrap;
  }
  .divider { flex: 0 0 2px; height: 190px; background: var(--brand-blue); margin-left: 10px; }
  .contact-block { padding-left: 18px; min-width: 0; }
  .person-name {
    font-family: "Michroma", sans-serif; font-size: 19px; font-weight: 400;
    letter-spacing: 2px; color: var(--ink-dark); text-transform: uppercase;
    margin-bottom: 8px; white-space: nowrap;
  }
  .person-name .surname { color: var(--brand-blue); }
  .person-role {
    font-family: "Didact Gothic", sans-serif; font-size: 17px;
    line-height: 1.25; color: var(--ink-gray); letter-spacing: 0.8px;
    margin-bottom: 12px; white-space: nowrap;
  }
  .contact-line {
    display: flex; align-items: center; gap: 10px;
    font-family: "Arimo", sans-serif; font-size: 16px; color: var(--ink-dark);
    margin-top: 8px; white-space: nowrap;
  }
  .contact-line svg { width: 20px; height: 14px; flex: none; }
  .footer-band {
    position: absolute; left: 0; right: 0; bottom: 0; height: 30px;
    display: flex; gap: 4px;
  }
  .footer-band .band-blue { background: var(--band-blue); }
  .footer-band .band-gray { background: var(--band-gray); }
  .band-left { flex: 0 0 296px; }
  .band-mid { flex: 0 0 272px; }
  .band-right { flex: 1; }
</style>
</head>
<body>
  <section class="card card-back" aria-label="Card back">
    <div class="brand-row">
      <span class="brand-mark"></span>
      <span class="brand-name">Whitcombe Advisors</span>
    </div>
    <p class="tagline">SMALL BUSINESS ACCOUNTING AND TAXES</p>
  </section>

  <section class="card card-front" aria-label="Card front">
    <div class="front-body">
      <div class="brand-block">
        <div class="brand-row">
          <span class="brand-mark"></span>
          <span class="brand-name">Whitcombe Advisors</span>
        </div>
        <p class="tagline">SMALL BUSINESS ACCOUNTING AND TAXES</p>
      </div>
      <div class="divider"></div>
      <div class="contact-block">
        <h1 class="person-name">Gerald <span class="surname">Whitcombe</span></h1>
        <p class="person-role">Certified Public Accountant<br>President Whitcombe Advisors</p>
        <p class="contact-line">
          <svg viewBox="0 0 20 14" aria-hidden="true">
            <path d="M1 4 Q10 -1 19 4 L17 6 L14 5 L14 3 Q10 2 6 3 L6 5 L3 6 Z" fill="var(--brand-blue)"/>
            <rect x="4" y="7" width="12" height="7" rx="1.5" fill="var(--brand-blue)"/>
          </svg>
          (555) 417-2863
        </p>
        <p class="contact-line">
          <svg viewBox="0 0 20 14" aria-hidden="true">
            <rect x="0.5" y="0.5" width="19" height="13" fill="var(--brand-blue)"/>
            <path d="M1 1 L10 8 L19 1" fill="none" stroke="#fff" stroke-width="1.4"/>
          </svg>
          GWhitcombe@WhitcombeAdvisors.example
        </p>
      </div>
    </div>
    <div class="footer-band">
      <span class="band-blue band-left"></span>
      <span class="band-gray band-mid"></span>
      <span class="band-blue band-right"></span>
    </div>
  </section>
</body>
</html>
```